Group Medical Practice needs stationery, business cards etc. designed

We need stationery designed for a multisite practice that offers primary medical, dental and behavioral healthcare. We would like a design that is consistent for letterhead, business cards, Microsoft Outlook stationery etc. We have attached our new logo design.

Business

```html
<!DOCTYPE html>
<html lang="en">
<head>
<meta charset="utf-8">
<title>Cedar Ridge Health Services – Letterhead</title>
<link href="https://fonts.googleapis.com/css2?family=Arimo:wght@400;700&display=swap" rel="stylesheet">
<style>
  :root {
    --canvas-bg: #f4f4f4;
    --paper: #ffffff;
    --sky: #dce9f3;
    --sky-soft: #eef4f9;
    --brand-blue: #1f6fb2;
    --faint-blue: #dde9f2;
    --faint-green: #eef4e2;
    --text: #4a4a4a;
    --rule: #c9d3dc;
  }
  * { margin: 0; padding: 0; box-sizing: border-box; }
  html, body {
    width: 1200px; height: 1000px; overflow: hidden;
    background: var(--canvas-bg);
    font-family: "Arimo", Arial, sans-serif;
  }
  .letterhead {
    position: absolute; left: 333px; top: 90px;
    width: 564px; height: 814px;
    background: var(--paper);
    overflow: hidden;
  }
  .header-art {
    position: absolute; left: 0; top: 0; width: 564px; height: 146px;
    background: linear-gradient(180deg, var(--sky) 0%, var(--sky-soft) 70%, var(--paper) 100%);
  }
  .header-logo {
    position: absolute; left: 0; top: 96px; width: 564px;
    display: flex; align-items: center; justify-content: center; gap: 7px;
  }
  .header-logo .mark {
    width: 10px; height: 10px; border-radius: 50%;
    background: var(--brand-blue);
  }
  .header-logo .name {
    color: var(--brand-blue);
    font-size: 17px; font-weight: 700; letter-spacing: 0.3px; line-height: 1;
  }
  .letter-body {
    position: absolute; left: 53px; top: 222px; width: 452px;
    color: var(--text); font-size: 10.9px; line-height: 17.2px;
    text-align: justify; hyphens: auto;
  }
  .letter-body p + p { margin-top: 17px; }
  .signature {
    position: absolute; right: 59px; top: 565px;
    text-align: right; color: var(--text);
    font-size: 10.9px; line-height: 17px;
  }
  .watermark-art {
    position: absolute; left: 45px; top: 600px; width: 460px; height: 108px;
    background: linear-gradient(180deg, var(--paper) 0%, var(--faint-green) 100%);
  }
  .faint-name {
    position: absolute; left: 0; top: 710px; width: 564px;
    text-align: center; color: var(--faint-blue);
    font-size: 40px; font-weight: 700; letter-spacing: 2px; line-height: 1;
  }
  .footer {
    position: absolute; left: 0; top: 763px; width: 564px; height: 51px;
    border-top: 1px solid var(--rule);
    display: flex; align-items: center; justify-content: center;
  }
  .footer-name {
    color: var(--brand-blue); font-size: 8.5px; font-weight: 700;
    padding-right: 12px; margin-right: 10px;
    border-right: 1px solid var(--brand-blue); line-height: 24px;
  }
  .footer-address { color: var(--text); font-size: 9px; }
</style>
</head>
<body>
  <main class="letterhead">
    <div class="header-art" role="img" aria-label="Pale blue sky band with a white mountain range silhouette"></div>
    <div class="header-logo">
      <span class="mark"></span>
      <span class="name">Cedar Ridge Health Services</span>
    </div>

    <section class="letter-body">
      <p>Lorem ipsum dolor sit amet, consectetur adipiscing elit. Donec orci purus, luctus vitae dignissim eu, iaculis sed purus. Vivamus faucibus, ipsum nec aliquet viverra, leo mauris condimentum ligula, sit amet sagittis enim ligula quis arcu. Nam egestas tortor id nisi porttitor mattis. In tortor ante, ultricies in suscipit a, tempus non massa. Vivamus et auctor mi. Fusce vel massa nulla. Phasellus nec eros mauris, et scelerisque orci. Donec malesuada orci vitae nulla accumsan porta a id massa. Quisque accumsan iaculis magna sit amet fringilla. Maecenas consequat, magna eget tincidunt semper, odio nibh rutrum mi, id feugiat ante nisi eu risus. Vestibulum nunc orci, rhoncus a placerat in, ultricies in mi. Cras mattis varius eros, vel fringilla nisi suscipit eget.</p>
      <p>Quisque scelerisque sagittis nulla at porttitor. Mauris a justo et tellus interdum tristique. Sed id augue vitae urna euismod commodo aliquet a quam. Pellentesque arcu velit, cursus et malesuada ut, consequat et diam. Nullam erat sem, rhoncus id ullamcorper vitae, rhoncus et arcu. In ultricies ultricies nulla, ut rutrum nisi iaculis at. Donec eu magna a metus ornare faucibus. Fusce aliquet faucibus ultricies. Morbi semper, est id tincidunt gravida, sem arcu adipiscing lacus, ac bibendum nulla leo eu purus. Quisque nec diam sed risus consectetur a ccumsan quis quis nibh. Vestibulum id purus lorem.</p>
    </section>

    <div class="signature">
      <div>Daniel Hartwell</div>
      <div>President and C.E.O</div>
    </div>

    <div class="watermark-art" role="img" aria-label="Faint pale green backdrop area above the watermark name"></div>
    <div class="faint-name">CEDAR RIDGE</div>

    <footer class="footer">
      <span class="footer-name">Cedar Ridge Health Services</span>
      <span class="footer-address">240 Maple Street Ste 104 | Millbrook, Virginia 24310</span>
    </footer>
  </main>
</body>
</html>
```